Business Card Trio Design

We need a set of business cards that all match but are not identical. We need one generic for the business and one for each of the two owners. We would like the cards to be similar to each other, but not identical. We have a logo and the colors of the logo are painstakingly chosen so if blue or green is used, we prefer our specific blue and green. Our logo pops better on a black background as well. We are open to double-sided, but it is not the top choice. We would love some either gold or silver accents that are in a foiled appearance. We sell uniforms (scrubs, culinary, EMT, police, fire, business, all types except kids and sports), shoes, equipment, and accessories. We also have facebook, pinterest, instagram, and twitter that we would like to have them follow and we offer splitwell in the store we would like the card to also advertise.

```html
<!DOCTYPE html>
<html lang="en">
<head>
<meta charset="utf-8">
<title>Verdant Workwear — Business Cards</title>
<link href="https://fonts.googleapis.com/css2?family=Cinzel:wght@500&family=Open+Sans:wght@400;600&display=swap" rel="stylesheet">
<style>
  :root {
    --bg-light: #a3a4a6;
    --bg-dark: #6d6e70;
    --card-black: #161617;
    --card-edge: #0b0b0c;
    --brand-blue: #7ea6cf;
    --brand-green: #1fa37f;
    --text-white: #f2f2f2;
    --ghost: #24272b;
  }
  * { margin: 0; padding: 0; box-sizing: border-box; }
  html, body { width: 1200px; height: 781px; overflow: hidden; }
  body {
    background: radial-gradient(ellipse at 50% 40%, var(--bg-light), var(--bg-dark));
    position: relative;
    font-family: "Open Sans", Arial, sans-serif;
  }
  .card {
    position: absolute;
    width: 500px;
    height: 286px;
    background: var(--card-black);
    border-radius: 18px;
    overflow: hidden;
    box-shadow: 0 14px 30px rgba(0,0,0,.35);
  }
  .card--front { left: 60px; top: 248px; }
  .card--back { left: 640px; top: 248px; }

  .ghost-circle {
    position: absolute;
    border-radius: 50%;
    background: var(--ghost);
  }
  .card--front .ghost-circle { width: 190px; height: 190px; right: -30px; top: 30px; }
  .card--back .ghost-circle { width: 300px; height: 300px; right: -90px; top: 20px; background: #1e1f21; }

  .wordmark {
    position: absolute;
    display: flex;
    align-items: center;
    gap: 10px;
    font-family: "Cinzel", Georgia, serif;
    font-weight: 500;
    color: var(--brand-blue);
    letter-spacing: 1px;
  }
  .wordmark__dot { border-radius: 50%; background: var(--brand-green); flex: none; }
  .card--front .wordmark { left: 32px; top: 26px; font-size: 22px; }
  .card--front .wordmark__dot { width: 20px; height: 20px; }
  .card--back .wordmark { left: 50%; top: 50%; transform: translate(-50%, -50%); font-size: 32px; white-space: nowrap; }
  .card--back .wordmark__dot { width: 30px; height: 30px; }

  .person { position: absolute; left: 32px; top: 80px; }
  .person__name {
    font-family: "Cinzel", Georgia, serif;
    font-size: 19px;
    color: var(--brand-blue);
    letter-spacing: .5px;
  }
  .person__title { font-size: 10px; color: var(--text-white); margin-top: 1px; }

  .rule {
    position: absolute;
    left: 32px; top: 124px;
    width: 420px; height: 1px;
    background: var(--brand-blue);
  }
  .contact { position: absolute; left: 32px; top: 134px; list-style: none; }
  .contact li {
    display: flex; align-items: center; gap: 6px;
    font-size: 11px; color: var(--text-white); line-height: 17px;
  }
  .contact svg { width: 10px; height: 10px; fill: var(--brand-green); flex: none; }

  .address {
    position: absolute;
    right: 40px; top: 168px;
    text-align: right;
    font-size: 11.5px;
    line-height: 17px;
    color: var(--text-white);
  }
  .wave { position: absolute; left: 0; bottom: 0; width: 500px; height: 90px; }
</style>
</head>
<body>

  <section class="card card--front" aria-label="Card front">
    <div class="ghost-circle"></div>
    <div class="wordmark"><span class="wordmark__dot"></span>Verdant Workwear</div>
    <div class="person">
      <p class="person__name">Martin Hale</p>
      <p class="person__title">President</p>
    </div>
    <div class="rule"></div>
    <ul class="contact">
      <li><svg viewBox="0 0 10 10"><path d="M2 0h2l1 3-1.5 1a6 6 0 0 0 2.5 2.5L7 5l3 1v2a2 2 0 0 1-2 2A8 8 0 0 1 0 2a2 2 0 0 1 2-2z"/></svg>(555) 014-2290</li>
      <li><svg viewBox="0 0 10 10"><path d="M0 2h10v6H0z M0 2l5 3.5L10 2" /></svg>hello@verdantworkwear.com</li>
      <li><svg viewBox="0 0 10 10"><circle cx="5" cy="5" r="5"/></svg>www.verdantworkwear.com</li>
    </ul>
    <p class="address">418 Harbor Point Plaza<br>Fairview, NC 28000</p>
    <svg class="wave" viewBox="0 0 500 90" preserveAspectRatio="none" aria-hidden="true">
      <path d="M0 18 C70 20 130 40 170 90 L0 90 Z" fill="var(--brand-blue)"/>
      <path d="M0 30 C60 32 120 50 160 90 L0 90 Z" fill="var(--brand-green)"/>
    </svg>
  </section>

  <section class="card card--back" aria-label="Card back">
    <div class="ghost-circle"></div>
    <div class="wordmark"><span class="wordmark__dot"></span>Verdant Workwear</div>
  </section>

</body>
</html>
```